Brisk Mend's Blow Their Mind Website

We own a group of cell phone and tablet repair shops in the bay area that is emerging into the mobile device insurance industry and want to develop a site that is clean, organized, and efficient at communicating who we are, the services we provide and the positive feedback we have been getting from our clients. As we enter into this new field of business, Our goal is to attract larger corporate accounts.

We want our home screen to have a big focus on the protection plan for the devices right away much like the home screen from these links:

http://www.velmorcove.com/

and also - https://us.keeplarnwick.com/smartphone-protection.html

We also need to make our repair services clear, here is a website of a company that does repair and we want to highlight both ends of the business.

ww.dolvafix.com

So the home screen will include the tab categories at the top of the screen
home/ protection /repair /about /contact

The first portion will be protection and as you scroll down there will be the next section about repair and following that will be information about the company.

Target Market(s)

Individuals that would be looking for pricing, clients that come to our store, but ultimately the heavy hitters we would want to attract would be larger corporate accounts so the message we want to communicate is professional, organized and credible in the services we provide.

Cell Phone

5+ page

Serif

34a6d7

Must have
• Eye catching, organized, with the wow factor that a business will look at our site and will be able to tell that we know what looks good and what grabs peoples attention. A large emphasis on the protection plan section like the links we provided and an organized home screen with the sections highlighted in the project description
• Tabs with links to different sections of the business such as protection that will go into detail about our protections plans and why our plan is best
• repair with a menu of the different prices we provide for different devices and services for that device
• an about us tab
• a contact us tab
Nice to have
• Artistic flow on the homescreen that the different sections flow together without looking too cookie cutter
• Wow factor
Should not have
• Clutter, confusion, disorganization, cheesy cookie cutter

```html
<!DOCTYPE html>
<html lang="en">
<head>
<meta charset="utf-8">
<title>Brisk Mend</title>
<link href="https://fonts.googleapis.com/css2?family=Open+Sans:wght@400;600;700&display=swap" rel="stylesheet">
<style>
:root{
  --blue:#34a6d7;
  --blue-dark:#2690c0;
  --ink:#3a3a3a;
  --muted:#8a8a8a;
  --line:#e2e2e2;
  --band:#ebebeb;
  --nav-dark:#1f3a4d;
  --base:#1d2a33;
  --white:#fff;
  --red:#e2463a;
}
*{box-sizing:border-box;margin:0;padding:0}
html,body{width:1200px;height:2788px;overflow:hidden}
body{font-family:"Open Sans",Arial,sans-serif;color:var(--ink);background:var(--white);font-size:13px;line-height:1.6;position:relative}
.wrap{width:960px;margin:0 auto;position:relative}
a{color:inherit;text-decoration:none}

.topbar{height:36px;background:var(--blue)}
.topbar ul{list-style:none;display:flex;height:36px}
.topbar li{padding:0 20px;line-height:36px;color:var(--white);font-weight:600;font-size:13px}
.topbar li.active{background:var(--nav-dark)}

.masthead{height:92px}
.masthead .wrap{display:flex;align-items:center;justify-content:space-between;height:92px}
.brand{display:flex;align-items:center;gap:12px;font-weight:700;font-size:30px;color:var(--blue)}
.brand-mark{width:34px;height:34px;border-radius:50%;background:var(--blue)}
.sitenav{display:flex;align-items:center;gap:22px;font-size:13px;color:var(--ink)}
.social{display:flex;gap:8px}
.social span{width:26px;height:26px;border-radius:50%;background:var(--red)}
.social span:first-child{background:var(--blue)}

.hero{height:492px;background:linear-gradient(120deg,#cfcac2 0%,#8a857d 35%,#3d3b38 55%,#9d978e 78%,#ddd8cf 100%)}

.features{height:92px;border-bottom:1px solid var(--line);margin-top:20px}
.features .wrap{display:flex;justify-content:space-between;height:72px;align-items:center;background:#f5f5f5;padding:0 24px}
.feature{display:flex;align-items:center;gap:12px}
.feature svg{width:38px;height:38px}
.feature b{display:block;font-size:14px}
.feature small{display:block;color:var(--muted);font-size:11px;line-height:1.3}

.intro{padding:34px 0 0}
.intro h2{color:var(--blue);font-size:20px;font-weight:600;margin-bottom:8px}
.intro p{color:var(--muted);font-size:13px;width:940px}

.services{display:flex;justify-content:space-between;margin-top:40px}
.service{width:216px;height:172px;background:var(--white);box-shadow:0 2px 8px rgba(0,0,0,.15);text-align:center;padding-top:26px}
.service svg{width:54px;height:54px}
.service h3{color:var(--blue);font-size:15px;font-weight:700;margin-top:14px}
.service a{display:block;font-size:11px;color:var(--muted);margin-top:18px}

.repair{margin-top:62px;display:flex;justify-content:space-between;height:470px}
.repair-text{width:440px}
.repair-text h2{color:var(--blue);font-size:20px;font-weight:600;margin-bottom:10px}
.repair-text p{color:var(--muted);margin-bottom:14px}
.repair-media{width:420px;display:flex;flex-direction:column;justify-content:space-between}
.photo{height:190px}
.photo-a{background:linear-gradient(135deg,#c9d8e4,#6b7e8e 50%,#e7ecef)}
.photo-b{background:linear-gradient(135deg,#5a3b2d,#c25340 45%,#3a5a8a 75%,#1e2b3a)}

.reviews{background:var(--band);height:300px;margin-top:58px}
.reviews .wrap{display:flex;justify-content:space-between;padding-top:38px}
.review{width:210px;text-align:center}
.bubble{width:200px;height:200px;border-radius:50%;background:var(--white);margin:0 auto;padding:40px 26px 0;font-size:11px;color:var(--muted);line-height:1.5}
.stars{color:#f2b01e;font-size:16px;letter-spacing:2px;margin-bottom:6px}
.review cite{display:block;font-style:normal;font-size:12px;color:var(--ink);margin-top:12px;font-weight:600}

.pricing{display:flex;justify-content:space-between;margin-top:40px;height:300px}
.phone{width:200px;height:290px;border-radius:26px;background:linear-gradient(160deg,#f58aa6,#e0416a)}
.price-table{width:360px}
.price-table h2{font-size:20px;color:var(--blue);font-weight:600;line-height:1}
.price-table h2 small{font-size:12px;color:var(--muted)}
table{width:100%;border-collapse:collapse;margin-top:10px;font-size:11px}
th{text-align:left;color:var(--muted);font-weight:600;padding:2px 0;border-bottom:1px solid var(--line)}
td{padding:1px 0;color:var(--ink)}
.note{font-size:10px;color:var(--muted);margin-top:8px;line-height:1.4}
.appointment{width:300px;height:230px;border:1px solid var(--line);padding:16px}
.appointment h3{font-size:15px;color:var(--ink);font-weight:700}
.appointment p{font-size:11px;color:var(--muted);margin-bottom:8px}
.field{height:24px;border:1px solid var(--line);margin-bottom:6px}
.btn{display:inline-block;background:var(--blue);color:var(--white);font-size:11px;font-weight:600;padding:4px 16px;margin-top:4px}

.footer{position:absolute;top:2332px;left:0;width:1200px;height:424px;background:var(--blue);color:var(--white)}
.footer .wrap{display:flex;justify-content:space-between;padding-top:50px}
.footer .col{width:210px}
.footer h4{font-size:14px;font-weight:700;margin-bottom:12px}
.footer li{list-style:none;font-size:12px;line-height:1.9;opacity:.92}
.copyright{position:absolute;top:2756px;left:0;width:1200px;height:32px;background:var(--base);color:#b7c3cb;text-align:center;font-size:11px;line-height:32px}
</style>
</head>
<body>

<nav class="topbar">
  <div class="wrap">
    <ul>
      <li class="active">Home</li>
      <li>About Us</li>
      <li>Protection</li>
      <li>Repair</li>
      <li>Contact</li>
    </ul>
  </div>
</nav>

<header class="masthead">
  <div class="wrap">
    <div class="brand"><span class="brand-mark"></span>Brisk Mend</div>
    <div class="sitenav">
      <a>Find a store</a><a>Blog</a><a>Heal My Device</a><a>Help</a>
      <div class="social"><span></span><span></span><span></span><span></span></div>
    </div>
  </div>
</header>

<section class="hero" role="img" aria-label="Technician's hands repairing an opened tablet on a workbench"></section>

<section class="features">
  <div class="wrap">
    <div class="feature">
      <svg viewBox="0 0 38 38"><rect x="11" y="4" width="16" height="30" rx="3" fill="none" stroke="#3a3a3a" stroke-width="2"/><circle cx="19" cy="29" r="1.6" fill="#3a3a3a"/></svg>
      <div><b>Cell Phone Repair</b><small>Fast, same day fixes</small></div>
    </div>
    <div class="feature">
      <svg viewBox="0 0 38 38"><path d="M19 4l12 5v9c0 8-5 13-12 16C12 31 7 26 7 18V9z" fill="none" stroke="#3a3a3a" stroke-width="2"/><path d="M13 19l4 4 8-8" fill="none" stroke="#34a6d7" stroke-width="2.4"/></svg>
      <div><b>Warranty</b><small>Every repair covered</small></div>
    </div>
    <div class="feature">
      <svg viewBox="0 0 38 38"><path d="M8 30C8 14 20 8 32 8c0 14-8 22-22 22z" fill="none" stroke="#3a3a3a" stroke-width="2"/><path d="M8 30l14-14" stroke="#34a6d7" stroke-width="2"/></svg>
      <div><b>Eco Friendly</b><small>Parts recycled safely</small></div>
    </div>
    <div class="feature">
      <svg viewBox="0 0 38 38"><circle cx="19" cy="19" r="13" fill="none" stroke="#3a3a3a" stroke-width="2"/><path d="M19 11v9l6 4" fill="none" stroke="#34a6d7" stroke-width="2.4"/></svg>
      <div><b>Services</b><small>Open seven days</small></div>
    </div>
  </div>
</section>

<main class="wrap">
  <section class="intro">
    <h2>Has your gadgets life just changed?</h2>
    <p>Have all facets of your life just been altered, signal lost and connection to the world has vanished. Handy as losing a arm and far fewer. All friends, family and peers feel gone, your gadget life going fast. Bring it to us and we'll have it working again so life and its moments return. Don't wait; visit a local Brisk Mend store and let us take care of your device.</p>
  </section>

  <section class="services">
    <div class="service">
      <svg viewBox="0 0 54 54"><rect x="17" y="6" width="20" height="40" rx="4" fill="none" stroke="#34a6d7" stroke-width="2.4"/><path d="M22 26h10M27 21v10" stroke="#34a6d7" stroke-width="2.4"/></svg>
      <h3>HEAL MY DEVICE</h3><a>» Read more</a>
    </div>
    <div class="service">
      <svg viewBox="0 0 54 54"><path d="M8 28l18-18h18v18L26 46z" fill="none" stroke="#34a6d7" stroke-width="2.4"/><circle cx="37" cy="17" r="3" fill="#34a6d7"/></svg>
      <h3>SELL MY DEVICE</h3><a>» Read more</a>
    </div>
    <div class="service">
      <svg viewBox="0 0 54 54"><path d="M6 10h8l6 24h22l5-16H17" fill="none" stroke="#34a6d7" stroke-width="2.4"/><circle cx="22" cy="42" r="3" fill="#34a6d7"/><circle cx="40" cy="42" r="3" fill="#34a6d7"/></svg>
      <h3>SHOP</h3><a>» Read more</a>
    </div>
    <div class="service">
      <svg viewBox="0 0 54 54"><rect x="8" y="18" width="38" height="26" fill="none" stroke="#34a6d7" stroke-width="2.4"/><path d="M8 18l19-10 19 10M20 44V30h14v14" fill="none" stroke="#34a6d7" stroke-width="2.4"/></svg>
      <h3>WHOLE SELLER</h3><a>» Read more</a>
    </div>
  </section>

  <section class="repair">
    <div class="repair-text">
      <h2>KeyCell Brisk Mend</h2>
      <p>Our smartphone damage? Then simply let KeyCell repair it. Located at 2870 Larnwick Road, Larnwick 95-0870. We can get your back online in no time. We repair cracked screens, water damage, charging ports, batteries, speakers and more. Whatever the trouble with your phone or tablet, our trained staff can find and fix it fast.</p>
      <p>At KeyCell Brisk Mend the client comes first. We understand your device is important to you. That's why we offer prompt repair service that is always courteous, honest and professional. We use quality parts and every repair we perform is backed by our warranty.</p>
      <p>Repairing your broken, damaged or defective smartphone has never been easier. Visit us today, and discover why we're bay area's favorite cell phone repair store.</p>
    </div>
    <div class="repair-media">
      <div class="photo photo-a" role="img" aria-label="Hands using tools to open a smartphone on a repair mat"></div>
      <div class="photo photo-b" role="img" aria-label="Smartphone with a colorful tiled home screen held in hand"></div>
    </div>
  </section>
</main>

<section class="reviews">
  <div class="wrap">
    <div class="review"><div class="bubble"><div class="stars">★★★★★</div>"Very nice! Didn't think I could get it fixed the same day, staff was friendly and quick. Phone looks new."</div><cite>Rob</cite></div>
    <div class="review"><div class="bubble"><div class="stars">★★★★★</div>"Great service! Phone screen fixed in an hour, price was fair and clear. Will return again."</div><cite>Elena</cite></div>
    <div class="review"><div class="bubble"><div class="stars">★★★★★</div>"So far so nice, staff was helpful and honest. Got my tablet back working better than before."</div><cite>Marcus</cite></div>
    <div class="review"><div class="bubble"><div class="stars">★★★★★</div>"Never knew repairs could be this simple. Booked online and walked out happy. Top shop."</div><cite>Dana</cite></div>
  </div>
</section>

<section class="wrap pricing">
  <div class="phone" role="img" aria-label="Pink smartphone shown from the front"></div>
  <div class="price-table">
    <h2>Nova 5S/5C <small>repair prices</small></h2>
    <table>
      <tr><th>Service</th><th>In Store</th><th>Mail-In</th></tr>
      <tr><td>Screen</td><td>$89</td><td>$99</td></tr>
      <tr><td>Front Glass/LCD</td><td>$99</td><td>$109</td></tr>
      <tr><td>Back Camera</td><td>$59</td><td>$69</td></tr>
      <tr><td>Battery</td><td>$49</td><td>$59</td></tr>
      <tr><td>Front Camera</td><td>$49</td><td>$59</td></tr>
      <tr><td>Home Button</td><td>$45</td><td>$55</td></tr>
      <tr><td>Headphone</td><td>$55</td><td>$65</td></tr>
      <tr><td>Power Button</td><td>$55</td><td>$65</td></tr>
      <tr><td>Volume Button</td><td>$55</td><td>$65</td></tr>
      <tr><td>USB Charge Port</td><td>$59</td><td>$69</td></tr>
    </table>
    <p class="note">*Additional labor applies to repairs that go to order.<br>**Pricing subject to change for some models.</p>
  </div>
  <div class="appointment">
    <h3>MAKE AN APPOINTMENT</h3>
    <p>Book a time and skip the line.</p>
    <div class="field"></div><div class="field"></div><div class="field"></div><div class="field"></div>
    <span class="btn">BOOK NOW</span>
  </div>
</section>

<footer class="footer">
  <div class="wrap">
    <div class="col"><h4>PROTECTION PLANS</h4><ul><li>Smartphones</li><li>Nova Warranty</li><li>Stellar Warranty</li><li>Halden One Warranty</li><li>Nexor Warranty</li><li>Drovix Warranty</li><li>Other Smartphone</li></ul></div>
    <div class="col"><h4>TABLETS</h4><ul><li>NovaTab Warranty</li><li>Stellar Warranty</li><li>Nexor Warranty</li><li>Marlow Slate Warranty</li><li>Other Tablet Warranty</li></ul></div>
    <div class="col"><h4>SITE LINKS</h4><ul><li>Help</li><li>My Profile</li><li>Clients Center</li><li>Velmor Cove Network</li><li>Tech Support</li><li>Blog Repairs</li><li>Business &amp; Education</li></ul></div>
    <div class="col"><h4>CONNECT WITH US</h4><ul><li>Circlefeed</li><li>Chirpline</li><li>Plusroom</li><li>Tubecast</li><li>Pinstack</li><li>Snapframe</li><li>Brisk Mend Blog</li></ul></div>
  </div>
</footer>
<div class="copyright">Copyright © 2013 - 2015 brisk mend</div>

</body>
</html>
```